Modern Minimalist photo holiday card

I need a few designs for a photo holiday card that is modern , minimalist yet chic. Some examples on the web of things that I like -

http://www.quillvorn.com/product/38214/flat_holiday_photo_cards_velvet_comet.html
http://www.quillvorn.com/product/39572/flat_holiday_photo_cards_bright_pine.html

http://www.zubeklo.com/frame-lumen-minimalist-holiday-card-collection/

Target Market(s)

Customers would be American educated professional living in big cities and suburbs. They will most likely be females from 20 to 50.

Industry/Entity Type

Product

Requirements
Must have
• The cards are 5 by 7 folded. I need the design to support 1 photo preferably taking up the whole space with stylized words. No traditional holiday bells etc. Just a hint of holiday is fine. Need 4 designs to begin with. Please quote for 4 distinct designs as a package. You can use any photo you want.

The users submit their photos so the designs should work with many different photos and should not depend on the content of the photo. Users will be able to change the location of text so text placement can depend on the photo. If the colors are coordinated with the photo please provide some alternate colors ( for user to choose)

```html
<!DOCTYPE html>
<html lang="en">
<head>
<meta charset="utf-8">
<title>Merry &amp; Bright Holiday Photo Card</title>
<link rel="stylesheet" href="https://fonts.googleapis.com/css2?family=Parisienne&display=swap">
<style>
  :root {
    --teal: #6aab98;
    --frame-line: #3b3d3d;
    --ink: #3a3a3a;
    --photo-light: #eceff0;
    --photo-mid: #d9c6b4;
    --photo-warm: #c79f82;
  }
  html, body {
    margin: 0;
    padding: 0;
    overflow: hidden;
    background: #ffffff;
  }
  .card {
    position: relative;
    width: 1200px;
    height: 857px;
    overflow: hidden;
  }
  .card__photo {
    position: absolute;
    inset: 0;
    background:
      radial-gradient(ellipse 55% 60% at 45% 55%, var(--photo-warm) 0%, var(--photo-mid) 45%, transparent 80%),
      linear-gradient(180deg, var(--photo-light) 0%, #e4e6e6 60%, #cfd2d2 100%);
  }
  .card__frame {
    position: absolute;
    inset: 0;
  }
  .card__greeting {
    position: absolute;
    left: 870px;
    top: 690px;
    width: 300px;
    transform: rotate(-30deg);
    transform-origin: center;
    font-family: "Parisienne", cursive;
    color: var(--ink);
    text-align: center;
    line-height: 1;
  }
  .card__greeting-title {
    display: block;
    font-size: 52px;
  }
  .card__greeting-year {
    display: block;
    font-size: 38px;
    margin-top: -2px;
  }
</style>
</head>
<body>
  <main class="card">
    <div class="card__photo" role="img" aria-label="Family photo: smiling parents with two young children hugging them from behind, against a pale sky"></div>

    <svg class="card__frame" width="1200" height="857" viewBox="0 0 1200 857" aria-hidden="true">
      <rect class="band band--top" x="0" y="0" width="1200" height="18" fill="var(--teal)"/>
      <rect class="band band--bottom" x="0" y="832" width="1200" height="25" fill="var(--teal)"/>
      <polygon class="corner-wedge" points="738,828 1200,560 1200,828" fill="var(--teal)"/>
      <g class="frame-lines" stroke="var(--frame-line)" stroke-width="5" fill="none">
        <line x1="0" y1="20" x2="1200" y2="20"/>
        <line x1="0" y1="828" x2="1200" y2="828"/>
        <line x1="24" y1="0" x2="24" y2="857"/>
        <line x1="1172" y1="0" x2="1172" y2="857"/>
      </g>
    </svg>

    <div class="card__greeting">
      <span class="card__greeting-title">Merry &amp; Bright</span>
      <span class="card__greeting-year">2013</span>
    </div>
  </main>
</body>
</html>
```